Im open to ideas.. I was thinking on my business cards aswell as my logo. a place for my name. email. phone number and abn..

ive attched a file with my business logo. which i dont love the colours.. i was think a dark background with charcoal letters so something along those colour schumes but im open to ideas..

Business

BRL Constructions

```html
<!DOCTYPE html>
<html lang="en">
<head>
<meta charset="utf-8">
<title>BRL Constructions – Business Card</title>
<link rel="stylesheet" href="https://fonts.googleapis.com/css2?family=Open+Sans:wght@400;700&family=Pinyon+Script&display=swap">
<style>
  :root {
    --backdrop: #e4e5e7;
    --card: #f9f9f8;
    --charcoal: #313134;
    --accent-line: #c9402c;
    --script-red: #c41c22;
    --ink: #2a2a2c;
    --rule: #5a5a5c;
  }
  * { box-sizing: border-box; margin: 0; padding: 0; }
  html, body {
    width: 1200px;
    height: 720px;
    overflow: hidden;
    background: var(--backdrop);
  }
  .stage {
    width: 1200px;
    height: 720px;
    display: flex;
    align-items: center;
    justify-content: center;
  }
  .business-card {
    position: relative;
    width: 380px;
    height: 620px;
    background: var(--card);
    overflow: hidden;
  }
  .band {
    position: absolute;
    left: 0;
    width: 100%;
    height: 92px;
    background: var(--charcoal);
  }
  .band--top { top: 0; border-bottom: 7px solid var(--accent-line); }
  .band--bottom { bottom: 0; border-top: 7px solid var(--accent-line); }

  .company {
    position: absolute;
    top: 128px;
    left: 150px;
    width: 196px;
  }
  .company-name {
    font-family: "Open Sans", sans-serif;
    font-weight: 700;
    font-size: 21px;
    letter-spacing: 1.5px;
    text-transform: uppercase;
    color: var(--ink);
    line-height: 1.1;
  }
  .company-rule {
    margin-top: 12px;
    height: 2px;
    background: var(--rule);
  }

  .person {
    position: absolute;
    top: 196px;
    left: 44px;
  }
  .first-name {
    font-family: "Pinyon Script", cursive;
    font-size: 96px;
    line-height: 1;
    color: var(--script-red);
  }
  .last-name {
    margin: -8px 0 0 84px;
    font-family: "Open Sans", sans-serif;
    font-weight: 400;
    font-size: 46px;
    letter-spacing: 1px;
    color: var(--ink);
    line-height: 1;
  }

  .contact {
    position: absolute;
    top: 384px;
    left: 64px;
    list-style: none;
    font-family: "Open Sans", sans-serif;
    font-size: 21px;
    line-height: 1.5;
    color: var(--ink);
  }
  .contact .phone { margin-left: 56px; }
  .contact .email { margin-left: 0; }
</style>
</head>
<body>
<main class="stage">
  <article class="business-card">
    <div class="band band--top"></div>

    <header class="company">
      <p class="company-name">BRL Constructions</p>
      <div class="company-rule"></div>
    </header>

    <section class="person">
      <p class="first-name">Liam</p>
      <p class="last-name">CARTER</p>
    </section>

    <ul class="contact">
      <li class="phone">555 555 555</li>
      <li class="email">youremail@email.com</li>
      <li class="abn">Abn Number</li>
    </ul>

    <div class="band band--bottom"></div>
  </article>
</main>
</body>
</html>
```